Banner Design

A law firm looking for a logo that can be used in a web banner that highlights the web address "peachsplitaid.example" and incorporates our law firms name- Brindle and Associates. Would prefer a design with softer green color like Russian Green.

A preliminary thought would be a boxed banner with a Brindle and Associates logo on either side of the web address "peachsplitaid.example".

Traditional and modern designs welcomed.
Updates

   Please make sure that "peachsplitaid.example" is the main focus of the banner.  All advertising is being done to brand that website address.  Our law firm name/logo needs to be incorporated but not the focal point.  This banner will be listed at the top of every web page.

Designers feel free to go with an over/under design with peachsplitaid.example going on top in a prominent position over our firm name. If that style sparks your creativity.  Remember this will be the banner design that will go on top of every page of the new website.        

                                I was thinking the firm name/logo on either side of the "peachsplitaid.example" would look balanced. But from the designs that I have received maybe it would look more balance with the "peachsplitaid.example" illustration over the firm name.

Target Market(s)

individuals 30-50

Industry/Entity Type

Law Firm

Logo Text

Brindle and Associates peachsplitaid.example

Logo styles of interest
Emblem Logo
Wordmark Logo

```html
<!DOCTYPE html>
<html lang="en">
<head>
<meta charset="utf-8">
<title>Brindle &amp; Associates — peachsplitaid.example</title>
<link rel="stylesheet" href="https://fonts.googleapis.com/css2?family=PT+Serif:wght@700&family=Roboto+Condensed:wght@600&display=swap">
<style>
  :root {
    --green-deep: #2c7565;
    --green-mid: #3f8c7b;
    --green-soft: #5fa594;
    --band-white: #ffffff;
    --ink: #111111;
    --text-light: #ffffff;
    --gavel-dark: #1f5a4c;
  }
  * { margin: 0; padding: 0; box-sizing: border-box; }
  html, body { width: 1200px; height: 174px; overflow: hidden; }
  .banner {
    position: relative;
    width: 1200px;
    height: 174px;
    overflow: hidden;
    background: linear-gradient(90deg, var(--green-mid) 0%, var(--green-soft) 45%, var(--green-mid) 75%, var(--green-deep) 100%);
  }
  .banner__rules {
    position: absolute; inset: 0;
    background: repeating-linear-gradient(180deg, rgba(255,255,255,0) 0 22px, rgba(255,255,255,0.06) 22px 24px);
  }
  .banner__band {
    position: absolute;
    left: 0; top: 60px;
    width: 692px; height: 54px;
    background: var(--band-white);
  }
  .firm-name {
    position: absolute;
    left: 34px; top: 60px;
    height: 54px;
    display: flex; align-items: center; gap: 10px;
    font-family: "PT Serif", serif;
    font-weight: 700;
    font-size: 21px;
    color: var(--green-deep);
    white-space: nowrap;
  }
  .firm-name__dot {
    width: 14px; height: 14px;
    border-radius: 50%;
    background: var(--green-deep);
  }
  .web-address {
    position: absolute;
    left: 280px; top: 64px;
    width: 408px; height: 46px;
    border-left: 2px solid var(--green-deep);
    display: flex; align-items: center; justify-content: center;
    font-family: "PT Serif", serif;
    font-weight: 700;
    font-size: 29px;
    letter-spacing: -0.5px;
    color: var(--ink);
  }
  .office-address {
    position: absolute;
    left: 734px; top: 110px;
    font-family: "Roboto Condensed", sans-serif;
    font-weight: 600;
    font-size: 17px;
    color: var(--text-light);
    white-space: nowrap;
  }
  .gavel-art {
    position: absolute;
    right: 6px; top: 0;
    width: 190px; height: 174px;
    background: radial-gradient(ellipse at 55% 60%, var(--gavel-dark) 0%, rgba(31,90,76,0.6) 45%, rgba(44,117,101,0) 75%);
  }
</style>
</head>
<body>
  <header class="banner">
    <div class="banner__rules"></div>
    <div class="banner__band"></div>
    <div class="firm-name"><span class="firm-name__dot"></span>Brindle &amp; Associates</div>
    <div class="web-address">www.peachsplitaid.example</div>
    <div class="office-address">Suite No. 410, Elm Row, Main City</div>
    <div class="gavel-art" role="img" aria-label="Photograph of a judge's gavel resting on its sound block"></div>
  </header>
</body>
</html>
```